Pipelining Product Supply Company Needs New Stationery

We need new stationery (letter head, with compliments slips & business card) for our industry leading pipe lining supply company. basically we sell product to other plumbers to carry out pipe relining.

Im looking for something, fresh, professional, sleek and modern at the same time.

Ive attached a copy of the logo and also some guidelines to follow for colours and fonts etc.

Target Market(s)

Plumbers

Industry/Entity Type

Plumbing

Font styles to use
Sans Serif

Requirements
Must have
• The logo, space for ABN, Address, Phone Number, website and email.
Nice to have
• Stand out from the crowd. To look sleep and professional.
Should not have
• Any other colours apart from what is on the guidelines.

```html
<!DOCTYPE html>
<html lang="en">
<head>
<meta charset="utf-8">
<title>Coastal Relining Supplies – Business Card</title>
<link rel="stylesheet" href="https://fonts.googleapis.com/css2?family=Open+Sans:wght@400;600&display=swap">
<style>
  :root {
    --bg: #e4e4e3;
    --white: #ffffff;
    --band: #ececec;
    --green: #7cbd1e;
    --green-light: #c3e98c;
    --green-dark: #4f8a25;
    --charcoal: #333333;
    --grey-text: #6e6e6e;
    --shadow: rgba(0,0,0,0.18);
  }
  * { box-sizing: border-box; margin: 0; padding: 0; }
  html, body { width: 1200px; height: 856px; overflow: hidden; }
  body {
    background: var(--bg);
    font-family: "Open Sans", Arial, sans-serif;
    display: flex; align-items: center; justify-content: center; gap: 50px;
  }
  .card {
    position: relative; width: 540px; height: 309px;
    border-radius: 24px; overflow: hidden;
    box-shadow: 0 12px 30px var(--shadow);
  }
  /* Front */
  .card-front { background: var(--white); }
  .card-front .art { position: absolute; inset: 0; }
  .front-brand {
    position: absolute; right: 40px; top: 60px;
    color: var(--green); font-weight: 600; font-size: 22px; letter-spacing: 0.5px;
    display: flex; align-items: center; gap: 10px; white-space: nowrap;
  }
  .front-brand .mark { width: 14px; height: 14px; border-radius: 50%; background: var(--green); }
  .person { position: absolute; left: 34px; top: 150px; }
  .person .name { color: var(--green); font-weight: 600; font-size: 17px; line-height: 1.1; }
  .person .role { color: var(--grey-text); font-size: 11px; letter-spacing: 1px; text-transform: uppercase; }
  .contact { position: absolute; font-size: 10.5px; color: var(--charcoal); line-height: 1.9; white-space: nowrap; }
  .contact li { list-style: none; display: flex; align-items: flex-start; gap: 7px; }
  .contact svg { width: 10px; height: 10px; margin-top: 5px; flex: none; }
  .contact-address { left: 34px; top: 198px; }
  .contact-phone { left: 250px; top: 146px; }
  .contact-web { left: 372px; top: 146px; }
  /* Back */
  .card-back {
    background: linear-gradient(180deg, var(--green-light) 0%, var(--green) 55%, var(--green-dark) 100%);
    display: flex; align-items: center; justify-content: center;
  }
  .back-brand {
    color: var(--white); font-weight: 600; font-size: 28px; letter-spacing: 0.5px;
    display: flex; align-items: center; gap: 12px; white-space: nowrap;
  }
  .back-brand .mark { width: 18px; height: 18px; border-radius: 50%; background: var(--white); }
</style>
</head>
<body>

<section class="card card-front" aria-label="Business card front">
  <svg class="art" viewBox="0 0 540 309" aria-hidden="true">
    <rect x="0" y="40" width="540" height="75" fill="var(--band)"/>
    <line x1="150" y1="132" x2="520" y2="100" stroke="var(--green)" stroke-width="1.2"/>
    <path d="M300 250 L540 222 L540 309 L300 309 Z" fill="var(--charcoal)"/>
    <rect x="0" y="296" width="540" height="13" fill="var(--charcoal)"/>
    <path d="M0 250 L380 250 Q400 250 400 270 L400 296 L0 296 Z" fill="var(--white)"/>
  </svg>

  <div class="front-brand"><span class="mark"></span>Coastal Relining Supplies</div>

  <div class="person">
    <p class="name">Example Name</p>
    <p class="role">Designation</p>
  </div>

  <ul class="contact contact-address">
    <li>
      <svg viewBox="0 0 10 10"><path d="M5 0a3.5 3.5 0 0 1 3.5 3.5C8.5 6 5 10 5 10S1.5 6 1.5 3.5A3.5 3.5 0 0 1 5 0z" fill="var(--green)"/><circle cx="5" cy="3.5" r="1.2" fill="var(--white)"/></svg>
      <span>Example Street, Suite 100,<br>Harbourton 4000</span>
    </li>
  </ul>

  <ul class="contact contact-phone">
    <li><svg viewBox="0 0 10 10"><path d="M1 3c1 3 3 5 6 6l1.5-1.5-2-1.5-1 1C4 6.5 3.5 6 3 5l1-1-1.5-2z" fill="var(--green)"/></svg>(07) 5550 1482</li>
    <li><svg viewBox="0 0 10 10"><rect x="1" y="3" width="8" height="6" rx="1" fill="var(--green)"/><rect x="3" y="1" width="4" height="3" fill="var(--green)"/></svg>(07) 5550 1496</li>
  </ul>

  <ul class="contact contact-web">
    <li><svg viewBox="0 0 10 10"><rect x="0.5" y="2" width="9" height="6" fill="var(--green)"/><path d="M0.5 2L5 5.5 9.5 2" stroke="var(--white)" fill="none"/></svg>info@coastalrelining.com.au</li>
    <li><svg viewBox="0 0 10 10"><circle cx="5" cy="5" r="4" fill="none" stroke="var(--green)" stroke-width="1.4"/><circle cx="5" cy="5" r="1.5" fill="var(--green)"/></svg>www.coastalrelining.com.au</li>
  </ul>
</section>

<section class="card card-back" aria-label="Business card back">
  <div class="back-brand"><span class="mark"></span>Coastal Relining Supplies</div>
</section>

</body>
</html>
```